Company Letter head for real estate company

need company letter head

You can use the logo that I submitted. no need to create a new one

• must have my address on it..38642 MARLOWE, BRAMLEY, MI 48203-1957, INFO@WRKMB.CA

```html
<!DOCTYPE html>
<html lang="en">
<head>
<meta charset="utf-8">
<title>Wrenmark Letterhead</title>
<link rel="stylesheet" href="https://fonts.googleapis.com/css2?family=Montserrat:wght@400;500;600&display=swap">
<style>
  :root {
    --backdrop: #e9eaec;
    --paper: #ffffff;
    --ink: #1f1f1f;
    --green-dark: #5a9140;
    --green-light: #8cc63f;
    --tree-tint: #eef2ea;
    --sig-tint: #dcdcdc;
  }
  * { box-sizing: border-box; margin: 0; padding: 0; }
  html, body {
    width: 1200px; height: 874px; overflow: hidden;
    background: var(--backdrop);
    font-family: "Montserrat", sans-serif;
    color: var(--ink);
  }
  .letterhead {
    position: absolute; left: 300px; top: 13px;
    width: 600px; height: 848px;
    background: var(--paper);
    box-shadow: 0 6px 24px rgba(0,0,0,0.12);
    overflow: hidden;
  }
  .brand {
    position: absolute; left: 48px; top: 56px;
    display: flex; align-items: center; gap: 10px;
  }
  .brand-dot { width: 18px; height: 18px; border-radius: 50%; background: var(--green-light); }
  .brand-name { font-size: 26px; font-weight: 600; letter-spacing: 1px; color: var(--green-dark); }
  .contact {
    position: absolute; right: 60px; top: 44px;
    border-left: 1.5px solid var(--green-dark);
    padding: 4px 0 10px 16px;
    font-size: 9.5px; line-height: 1.55; letter-spacing: 0.3px;
    list-style: none;
  }
  .contact li { display: flex; align-items: center; gap: 6px; }
  .contact svg { width: 9px; height: 9px; fill: var(--green-light); }
  .letter {
    position: absolute; left: 64px; top: 180px; right: 56px;
    font-size: 10.5px; line-height: 1.6;
  }
  .recipient { margin-bottom: 2px; }
  .letter p { margin-bottom: 16px; }
  .closing { margin-top: 4px; }
  .signature { margin-top: 10px; width: 130px; height: 44px; background: var(--sig-tint); border-radius: 4px; opacity: .6; }
  .tree-art {
    position: absolute; left: 190px; bottom: 20px;
    width: 220px; height: 270px;
    background: radial-gradient(ellipse at center, var(--tree-tint) 0%, rgba(238,242,234,0) 72%);
  }
  .swoosh { position: absolute; inset: 0; width: 600px; height: 848px; }
</style>
</head>
<body>
  <main class="letterhead">
    <div class="brand">
      <span class="brand-dot"></span>
      <span class="brand-name">WRENMARK</span>
    </div>

    <ul class="contact">
      <li>38642 MARLOWE,</li>
      <li>BRAMLEY, MI</li>
      <li><svg viewBox="0 0 10 10"><path d="M2 0l2 2-1 1.5c.6 1.4 2 2.8 3.5 3.5L8 6l2 2-1.5 2C4 9.5.5 6 0 1.5z"/></svg>48203-1957</li>
      <li><svg viewBox="0 0 10 10"><path d="M0 2h10v6H0zM0 2l5 3.5L10 2"/></svg>INFO@WRKMB.CA</li>
      <li><svg viewBox="0 0 10 10"><circle cx="5" cy="5" r="5"/></svg>WWW.WRKMB.CA</li>
    </ul>

    <div class="tree-art" role="img" aria-label="Faint tree illustration"></div>

    <svg class="swoosh" viewBox="0 0 600 848" aria-hidden="true">
      <path d="M0 848 C200 836 420 790 525 680 C450 790 260 842 50 848 Z" fill="var(--green-light)"/>
      <path d="M48 848 C270 838 480 795 600 690 L600 848 Z" fill="var(--green-dark)"/>
    </svg>

    <section class="letter">
      <div class="recipient">
        Mr/s<br>First Name and Last Name<br>Company Name<br>Address
      </div>
      <p>Lorem Ipsum is simply dummy text of the printing and typesetting industry. Lorem Ipsum has been the industry's standard dummy text ever since the 1500s, when an unknown printer took a galley of type and scrambled it to make a type specimen book. It has survived not only five centuries, but also the leap into electronic typesetting, remaining essentially unchanged. It was popularised in the 1960s.</p>
      <p>The standard chunk of Lorem Ipsum used since the 1500s is reproduced below for those interested. Sections 1.10.32 and 1.10.33 from "de Finibus Bonorum et Malorum" by Cicero are also reproduced in their exact original form, accompanied by English versions from the 1914 translation by H. Rackham. Lorem ipsum dolor sit amet, consectetur adipiscing elit, sed do eiusmod tempor incididunt ut labore et dolore magna aliqua.</p>
      <p>It is a long established fact that a reader will be distracted by the readable content of a page when looking at its layout. The point of using Lorem Ipsum is that it has a more-or-less normal distribution of letters, as opposed to using 'Content here, content here', making it look like readable English. Many desktop publishing packages and web page editors now.</p>
      <div class="closing">Your Sincerely,</div>
      <div class="signature" role="img" aria-label="Handwritten signature"></div>
    </section>
  </main>
</body>
</html>
```